Boys overnight camp needs a flyer in Russian Language

We're are a boys overnight camp in Ukraine. The flyer needs to portray the camp as an extreme, high intensity, fun camp with lots of exciting activities. The flyer is to promote registration. The text needed is as follows:
( Place the letters- в”н " -in the top right corner)
Лагерь “Бор Светлый Tova”
Еврейских мальчиков
возраст 7-18 лет
30 июня -20 июля.
-увлекательные программы
-Игры, конкурсы, соревнования
-призы и подарки
походы
Пейнтбол,
Аквапарк,
Боулинг,
Каток,
Шашлыки,
Театеральные и цирковые представления,
Пляж и аттракционы
Тематически вечера у костра,
Баскетбол,
Футбол,
Волейбол,
И многое другое…
Общение с носителями англиского и иврита.
самые яркие впечатления лета 2015 в лагере бор светлый в украине!
Контакты:
050 713 5890
Больше информации: www.lagertovamir.com
С. ПОДЛЕСОВКА, ЖИТОМИРСКАЯ ОБЛАСТЬ

```html
<!DOCTYPE html>
<html lang="ru">
<head>
<meta charset="utf-8">
<title>Лагерь «Бор Светлый Tova»</title>
<link rel="stylesheet" href="https://fonts.googleapis.com/css2?family=Kelly+Slab&family=Ruslan+Display&display=swap">
<style>
  :root {
    --sun-yellow: #ffd23c;
    --sun-orange: #f7a21e;
    --deep-orange: #ec6a12;
    --title-green: #c9e23a;
    --ink: #2a2410;
    --banner-red: #c4161c;
    --banner-dark: #7a0a0e;
    --wine: #8e1a1f;
    --footer-yellow: #ffe14a;
    --slogan-red: #b3121a;
    --white: #ffffff;
  }
  html, body { margin: 0; padding: 0; overflow: hidden; }
  body { width: 852px; height: 1200px; background: #ffffff; }
  .flyer {
    position: relative; width: 852px; height: 1200px; overflow: hidden;
    font-family: "Kelly Slab", serif;
    background: repeating-conic-gradient(from 0deg at 760px 300px, var(--sun-yellow) 0deg 9deg, var(--sun-orange) 9deg 18deg);
  }
  .backdrop { position: absolute; inset: 0; }
  .mark {
    position: absolute; top: 14px; right: 26px; font-size: 22px; color: var(--ink); letter-spacing: 1px;
  }
  .title {
    position: absolute; top: 48px; left: 0; width: 852px; margin: 0; text-align: center;
    font-family: "Ruslan Display", serif; font-weight: 400; font-size: 44px; color: var(--title-green);
    -webkit-text-stroke: 2px var(--ink); text-shadow: 3px 3px 0 var(--ink); letter-spacing: 1px;
  }
  .banner {
    position: absolute; left: 0; color: var(--white); font-size: 24px; font-variant: small-caps;
    background: linear-gradient(var(--banner-red), var(--banner-dark));
    box-shadow: 4px 4px 0 rgba(0,0,0,.35); display: flex; align-items: center; justify-content: center;
  }
  .banner--audience { top: 148px; width: 395px; height: 40px; }
  .banner--age { top: 196px; width: 345px; height: 44px; font-size: 26px; }
  .burst { position: absolute; left: 0; top: 230px; }
  .dates {
    position: absolute; left: 55px; top: 305px; width: 160px; text-align: center; font-size: 25px; line-height: 1.15;
    color: var(--banner-red); transform: rotate(-22deg);
  }
  .brand { position: absolute; left: 435px; top: 150px; width: 300px; height: 300px; }
  .brand-circle { position: absolute; inset: 0; border-radius: 50%; background: var(--wine); }
  .brand-name {
    position: absolute; inset: 0; display: flex; align-items: center; justify-content: center; text-align: center;
    color: var(--white); font-size: 34px; line-height: 1.15; padding: 40px; box-sizing: border-box;
  }
  .photo { position: absolute; border-radius: 50%; box-sizing: border-box; border: 7px solid; }
  .photo--banana { left: 17px; top: 612px; width: 156px; height: 156px; border-color: var(--deep-orange); background: linear-gradient(#9cc7e4, #3f86b4 60%, #e9d84a); }
  .photo--buggies { left: 202px; top: 530px; width: 180px; height: 180px; border-color: #8aa22b; background: linear-gradient(#bfe0f4, #8fb6c9 45%, #c8b48a); }
  .photo--karting { left: 390px; top: 610px; width: 162px; height: 162px; border-color: var(--wine); background: linear-gradient(#6f8a4c, #3b3b3b 60%, #7a7a7a); }
  .photo--football { left: 170px; top: 705px; width: 192px; height: 192px; border-color: #6dbfc0; background: linear-gradient(#8eae6c, #95906a 55%, #b1a579); }
  .photo--friends { left: 10px; top: 822px; width: 146px; height: 146px; border-color: #f2e21b; background: linear-gradient(#5f8a4a, #8c8c8c 60%, #a9a9a9); }
  .photo--slides { left: 148px; top: 905px; width: 142px; height: 142px; border-color: var(--banner-red); background: linear-gradient(#b7d5e6, #f0c21c 55%, #4a8fc7); }
  .photo--paintball { left: 303px; top: 865px; width: 164px; height: 164px; border-color: var(--deep-orange); background: linear-gradient(#c9dcef, #5f7f3e 50%, #5b5c3a); }
  .activities {
    position: absolute; right: 12px; top: 528px; margin: 0; padding: 0; list-style: none; text-align: right;
    font-size: 22px; line-height: 30.6px; color: var(--ink); font-variant: small-caps;
  }
  .slogan {
    position: absolute; left: 0; top: 1056px; width: 852px; margin: 0; text-align: center;
    color: var(--slogan-red); font-size: 22px; line-height: 31px; font-variant: small-caps;
  }
  .footer {
    position: absolute; left: 0; top: 1120px; width: 852px; height: 80px;
    background: linear-gradient(var(--banner-red), var(--banner-dark));
    color: var(--footer-yellow); font-size: 23px; line-height: 33px; font-variant: small-caps;
  }
  .footer-contacts { position: absolute; left: 20px; top: 8px; }
  .footer-info { position: absolute; right: 14px; top: 8px; text-align: right; }
</style>
</head>
<body>
<main class="flyer">
  <svg class="backdrop" width="852" height="1200" viewBox="0 0 852 1200" aria-hidden="true">
    <defs>
      <radialGradient id="meadow" cx="430" cy="720" r="520" gradientUnits="userSpaceOnUse">
        <stop offset="0" stop-color="#eef27a"/>
        <stop offset="1" stop-color="#b7cf33"/>
      </radialGradient>
    </defs>
    <path d="M0 478 C 220 455, 520 455, 852 430 L852 1200 L0 1200 Z" fill="var(--deep-orange)"/>
    <path d="M0 520 C 230 495, 520 492, 852 470 L852 1200 L0 1200 Z" fill="url(#meadow)"/>
    <g fill="#ffffff" opacity="0.18">
      <polygon points="430,720 0,560 0,610"/>
      <polygon points="430,720 0,760 0,820"/>
      <polygon points="430,720 0,980 0,1050"/>
      <polygon points="430,720 250,1118 330,1118"/>
      <polygon points="430,720 560,1118 640,1118"/>
      <polygon points="430,720 852,980 852,1050"/>
      <polygon points="430,720 852,700 852,760"/>
      <polygon points="430,720 700,480 780,475"/>
      <polygon points="430,720 300,500 370,495"/>
    </g>
  </svg>

  <div class="mark">в”н</div>
  <h1 class="title">Лагерь “Бор Светлый Tova”</h1>

  <div class="banner banner--audience">Еврейских мальчиков возраст</div>
  <div class="banner banner--age">7-18 лет</div>

  <svg class="burst" width="300" height="260" viewBox="0 0 300 260" aria-hidden="true">
    <defs>
      <radialGradient id="blast" cx="0.45" cy="0.5" r="0.55">
        <stop offset="0" stop-color="#ffe23a"/>
        <stop offset="0.55" stop-color="#f7a21e"/>
        <stop offset="1" stop-color="#ec5a12"/>
      </radialGradient>
    </defs>
    <polygon fill="url(#blast)" points="135,5 160,80 240,20 195,100 300,95 205,140 285,215 185,170 175,255 140,180 80,250 95,165 5,200 70,130 0,70 90,95 60,15 120,75"/>
  </svg>
  <div class="dates">30 июня<br>- 20 июля</div>

  <div class="brand">
    <div class="brand-circle"></div>
    <div class="brand-name">Бор Светлый Tova</div>
  </div>

  <div class="photo photo--banana" role="img" aria-label="Фото: мальчики катаются на банане по морю"></div>
  <div class="photo photo--buggies" role="img" aria-label="Фото: квадроциклы и багги на берегу"></div>
  <div class="photo photo--karting" role="img" aria-label="Фото: картинг"></div>
  <div class="photo photo--football" role="img" aria-label="Фото: игра в футбол на поле"></div>
  <div class="photo photo--friends" role="img" aria-label="Фото: ребята в парке"></div>
  <div class="photo photo--slides" role="img" aria-label="Фото: горки аквапарка"></div>
  <div class="photo photo--paintball" role="img" aria-label="Фото: команда на пейнтболе"></div>

  <ul class="activities">
    <li>увлекательные программы</li>
    <li>Игры, конкурсы, соревнования</li>
    <li>призы и подарки</li>
    <li>походы</li>
    <li>Пейнтбол,</li>
    <li>Аквапарк,</li>
    <li>Боулинг,</li>
    <li>Каток,</li>
    <li>Шашлыки,</li>
    <li>Театеральные и цирковые</li>
    <li>представления,</li>
    <li>Пляж и аттракционы</li>
    <li>Тематически вечера у костра,</li>
    <li>Баскетбол,</li>
    <li>Футбол,</li>
    <li>Волейбол,</li>
    <li>И многое другое…</li>
  </ul>

  <p class="slogan">Общение с носителями англиского и иврита.<br>самые яркие впечатления лета 2015 в лагере бор светлый в украине!</p>

  <footer class="footer">
    <div class="footer-contacts">Контакты:<br>050 713 5890</div>
    <div class="footer-info">Больше информации: www.lagertovamir.com<br>С. ПОДЛЕСОВКА, ЖИТОМИРСКАЯ ОБЛАСТЬ</div>
  </footer>
</main>
</body>
</html>
```